Design Template for use with our Career Cluster Maps

***Update 11/24*** - Please see K7M Future Set Model (attached) for color scheme and targeted look and feel. Also, focus on content displayed in the Construction Cluster document (attached). All information displayed in the Construction Cluster document needs to be included in the design. Need a clean, simple design. Unique ideas for organizing content are welcomed.

We need a unique design for our curriculum maps. I have two copies that are models, both are good but are not unique to us as a company. We provide the data that allows the templates to be filled in by clients, so don't worry about the actual data, just what can we design around how the data is displayed. Our main website is ladderforwork.example , feel free to use anything from that site as well as the colors. I am attaching the 2 designs as well as some unique pictures that can be incorporated. The design when final will go into our software platform and the data will be pulled and placed for schools to use automatically, again looking for a design that captures the idea between the job market and job preparedness. I have added an additional document that shows "all the pathways" and how our software pulls the data and puts on a template. The template we desire needs to be updated, the two additional files show how our clients have tried to update the template with a better look and feel. We want a better look and feel in our platform.
Updates

Please post the design as a PDF but we need the In-Design files so that we can edit and use within our system

```html
<!DOCTYPE html>
<html lang="en">
<head>
<meta charset="utf-8">
<title>K7M Career Clusters and Pathways</title>
<link rel="stylesheet" href="https://fonts.googleapis.com/css2?family=Open+Sans:wght@400;600;700&family=Raleway:wght@400;600&display=swap">
<style>
:root{
  --orange:#d9892b;
  --orange-soft:#e9a24a;
  --navy:#1d2b4c;
  --blue:#3f6fa3;
  --bullet:#3d86c6;
  --ink:#2a2a2a;
  --page:#ffffff;
  --foot:#eef0f3;
}
*{box-sizing:border-box;margin:0;padding:0}
html,body{width:1200px;height:2496px;overflow:hidden;background:var(--page);font-family:"Open Sans",Arial,sans-serif;color:var(--ink)}
.page{position:relative;width:1200px;height:2496px}

.masthead{position:relative;height:220px;background:linear-gradient(90deg,#3a3b3f,#6a6c70 50%,#3a3b3f)}
.masthead-photo{position:absolute;inset:0;background:linear-gradient(180deg,rgba(255,255,255,.0),rgba(0,0,0,.25))}
.brand{position:absolute;top:26px;left:50%;transform:translateX(-50%);display:flex;align-items:center;gap:10px;color:#fff;font-weight:700;font-size:22px;letter-spacing:2px}
.brand-mark{width:22px;height:22px;background:var(--orange)}
.masthead-title{position:absolute;top:102px;left:0;right:0;text-align:center;color:#fff;font-family:"Raleway",sans-serif;font-size:40px;font-weight:400}
.masthead-sub{position:absolute;top:160px;left:150px;right:150px;text-align:center;color:#fff;font-size:12px;line-height:1.5}
.masthead-sub em{font-style:normal;color:var(--orange-soft);font-weight:600}

.heading{height:120px;display:flex;align-items:center;justify-content:center;font-family:"Raleway",sans-serif;font-size:64px;font-weight:400;color:var(--navy)}
.heading span{color:var(--orange);margin-left:16px}

.clusters{display:grid;grid-template-columns:1fr 1fr;column-gap:30px;row-gap:18px;padding:10px 40px 0;
  grid-template-rows:230px 200px 225px 225px 205px 225px 240px 280px}
.cluster{display:flex;flex-direction:column;border:1px solid #e6e6e6}
.cluster-title{background:var(--orange);color:#fff;font-size:22px;font-weight:600;padding:8px 16px;height:44px;white-space:nowrap}
.cluster-body{flex:1;display:flex;gap:16px;padding:12px}
.cluster-photo{width:170px;flex:none;background:linear-gradient(135deg,#9aa7b4,#c9b79e);}
.pathways{list-style:none;font-size:15px;line-height:1.35}
.pathways li{position:relative;padding-left:22px;margin-bottom:2px}
.pathways li::before{content:"";position:absolute;left:0;top:4px;width:13px;height:13px;background:var(--bullet);border-radius:2px}

.site-band{position:absolute;top:2330px;left:0;right:0;height:62px;background:var(--blue);color:#fff;text-align:center;font-size:24px;line-height:62px;font-weight:600}
.site-foot{position:absolute;top:2392px;left:0;right:0;bottom:0;background:var(--foot)}
</style>
</head>
<body>
<div class="page">
  <header class="masthead">
    <div class="masthead-photo" role="img" aria-label="Photo of students in a classroom setting"></div>
    <div class="brand"><span class="brand-mark"></span>K7M</div>
    <h1 class="masthead-title">Enhancing education planning</h1>
    <p class="masthead-sub">K7M Future Set helps schools connect learners with <em>in-demand careers</em> and the data, resources &amp; materials they need to <em>guide students on the pathway to career readiness.</em></p>
  </header>

  <h2 class="heading">Career Clusters<span>and Pathways</span></h2>

  <main class="clusters">
    <section class="cluster"><h3 class="cluster-title">Agriculture, Food &amp; Natural Resources</h3>
      <div class="cluster-body"><div class="cluster-photo" role="img" aria-label="Photo of farm work"></div>
      <ul class="pathways"><li>Agribusiness Systems</li><li>Animal Systems</li><li>Environmental Service Systems</li><li>Food Products &amp; Processing Systems</li><li>Natural Resources Systems</li><li>Plant Systems</li><li>Power, Structural &amp; Technical Systems</li></ul></div></section>

    <section class="cluster"><h3 class="cluster-title">Government &amp; Public Administration</h3>
      <div class="cluster-body"><div class="cluster-photo" role="img" aria-label="Photo of a government building"></div>
      <ul class="pathways"><li>Foreign Service</li><li>Governance</li><li>National Security</li><li>Planning</li><li>Public Management &amp; Administration</li><li>Regulation</li><li>Revenue &amp; Taxation</li></ul></div></section>

    <section class="cluster"><h3 class="cluster-title">Architecture &amp; Construction</h3>
      <div class="cluster-body"><div class="cluster-photo" role="img" aria-label="Photo of a construction worker"></div>
      <ul class="pathways"><li>Construction</li><li>Design/Pre-Construction</li><li>Maintenance/Operations</li></ul></div></section>

    <section class="cluster"><h3 class="cluster-title">Health Science</h3>
      <div class="cluster-body"><div class="cluster-photo" role="img" aria-label="Photo of medical staff"></div>
      <ul class="pathways"><li>Biotechnology Research &amp; Development</li><li>Diagnostic Services</li><li>Health Informatics</li><li>Support Services</li><li>Therapeutic Services</li></ul></div></section>

    <section class="cluster"><h3 class="cluster-title">Arts, A/V Technology &amp; Communications</h3>
      <div class="cluster-body"><div class="cluster-photo" role="img" aria-label="Photo of media production equipment"></div>
      <ul class="pathways"><li>A/V Technology &amp; Film</li><li>Journalism &amp; Broadcasting</li><li>Performing Arts</li><li>Printing Technology</li><li>Telecommunications</li><li>Visual Arts</li></ul></div></section>

    <section class="cluster"><h3 class="cluster-title">Hospitality &amp; Tourism</h3>
      <div class="cluster-body"><div class="cluster-photo" role="img" aria-label="Photo of hotel service staff"></div>
      <ul class="pathways"><li>Lodging</li><li>Recreation, Amusements &amp; Attractions</li><li>Restaurants &amp; Food/Beverage Services</li><li>Travel &amp; Tourism</li></ul></div></section>

    <section class="cluster"><h3 class="cluster-title">Business, Management &amp; Administration</h3>
      <div class="cluster-body"><div class="cluster-photo" role="img" aria-label="Photo of an office meeting"></div>
      <ul class="pathways"><li>Administrative Support</li><li>Business Information Management</li><li>General Management</li><li>Human Resources Management</li><li>Operations Management</li></ul></div></section>

    <section class="cluster"><h3 class="cluster-title">Human Services</h3>
      <div class="cluster-body"><div class="cluster-photo" role="img" aria-label="Photo of a counselling session"></div>
      <ul class="pathways"><li>Consumer Services</li><li>Counseling &amp; Mental Health Services</li><li>Early Childhood Development &amp; Services</li><li>Family &amp; Community Services</li><li>Personal Care Services</li></ul></div></section>

    <section class="cluster"><h3 class="cluster-title">Education &amp; Training</h3>
      <div class="cluster-body"><div class="cluster-photo" role="img" aria-label="Photo of a teacher with students"></div>
      <ul class="pathways"><li>Administration &amp; Administrative Support</li><li>Professional Support Services</li><li>Teaching/Training</li></ul></div></section>

    <section class="cluster"><h3 class="cluster-title">Information Technology</h3>
      <div class="cluster-body"><div class="cluster-photo" role="img" aria-label="Photo of a person at a computer"></div>
      <ul class="pathways"><li>Information Support &amp; Services</li><li>Network Systems</li><li>Programming &amp; Software Development</li><li>Web &amp; Digital Communications</li></ul></div></section>

    <section class="cluster"><h3 class="cluster-title">Finance</h3>
      <div class="cluster-body"><div class="cluster-photo" role="img" aria-label="Photo of financial documents"></div>
      <ul class="pathways"><li>Accounting</li><li>Banking Services</li><li>Business Finance</li><li>Insurance</li><li>Securities &amp; Investments</li></ul></div></section>

    <section class="cluster"><h3 class="cluster-title">Law, Public Safety, Corrections &amp; Security</h3>
      <div class="cluster-body"><div class="cluster-photo" role="img" aria-label="Photo of a legal professional"></div>
      <ul class="pathways"><li>Correction Services</li><li>Emergency &amp; Fire Management Services</li><li>Law Enforcement Services</li><li>Legal Services</li><li>Security &amp; Protective Services</li></ul></div></section>

    <section class="cluster"><h3 class="cluster-title">Manufacturing</h3>
      <div class="cluster-body"><div class="cluster-photo" role="img" aria-label="Photo of a factory worker"></div>
      <ul class="pathways"><li>Health, Safety &amp; Environmental Assurance</li><li>Logistics &amp; Inventory Control</li><li>Maintenance, Installation &amp; Repair</li><li>Manufacturing Production Process Development</li><li>Production</li><li>Quality Assurance</li></ul></div></section>

    <section class="cluster"><h3 class="cluster-title">Science, Technology, Engineering &amp; Mathematics</h3>
      <div class="cluster-body"><div class="cluster-photo" role="img" aria-label="Photo of a laboratory"></div>
      <ul class="pathways"><li>Engineering &amp; Technology</li><li>Science &amp; Mathematics</li></ul></div></section>

    <section class="cluster"><h3 class="cluster-title">Marketing</h3>
      <div class="cluster-body"><div class="cluster-photo" role="img" aria-label="Photo of a marketing team"></div>
      <ul class="pathways"><li>Marketing Communications</li><li>Marketing Management</li><li>Marketing Research</li><li>Merchandising</li><li>Professional Sales</li></ul></div></section>

    <section class="cluster"><h3 class="cluster-title">Transportation, Distribution &amp; Logistics</h3>
      <div class="cluster-body"><div class="cluster-photo" role="img" aria-label="Photo of a freight warehouse"></div>
      <ul class="pathways"><li>Facility &amp; Mobile Equipment Maintenance</li><li>Health, Safety &amp; Environmental Management</li><li>Logistics Planning &amp; Management Services</li><li>Sales &amp; Service</li><li>Transportation Operations</li><li>Transportation Systems/Infrastructure Planning, Management &amp; Regulation</li><li>Warehousing &amp; Distribution Center Operations</li></ul></div></section>
  </main>

  <footer>
    <div class="site-band">ladderforwork.example</div>
    <div class="site-foot"></div>
  </footer>
</div>
</body>
</html>
```